Doors for Chiropractic Office

In my chiropractic office I have 6 treatment rooms and 2 massage rooms. The entire office is going through a remodel. The overall color scheme is very earth tones but in order to add some color, the 6 doors to the treatment rooms will all be a separate color (Red, Blue, Yellow, Green etc)
I need to number each room 1,2,3,4,5,6 and the 2 massage rooms. I had the idea of putting a giant number on each door, so I am looking for some graphic ideas for that project.
The rooms are located with 4 on each side of a long hallway with the 2 massage rooms at the end.
The purpose of numbering each door is to direct the patients where to go.
I have uploaded pictures of the hall way. Pardon the dust since we are under construction but hopefully it gives you an idea of the layout. The door colors will change as stated above.

Requirements
Nice to have
• I would like to see someone come up with a design where each number for the doors are created out of vertebrae's.

```html
<!DOCTYPE html>
<html lang="en">
<head>
<meta charset="utf-8">
<title>Treatment Room Door Numbers</title>
<link rel="stylesheet" href="https://fonts.googleapis.com/css2?family=Barlow+Condensed:wght@600&family=Questrial&display=swap">
<style>
  :root {
    --backdrop: #5f5f5f;
    --room-one: #ffcb00;
    --room-two: #f2660a;
    --room-three: #f20405;
    --room-four: #ee2a7e;
    --room-five: #133883;
    --room-six: #05ae9c;
    --ink: #ffffff;
  }
  * { margin: 0; padding: 0; box-sizing: border-box; }
  html, body {
    width: 1200px;
    height: 1200px;
    overflow: hidden;
    background: var(--backdrop);
  }
  .door-set {
    position: relative;
    width: 1200px;
    height: 1200px;
  }
  .door-panel {
    position: absolute;
    width: 230px;
    height: 507px;
    overflow: hidden;
  }
  .door-panel--one   { left: 186px; top: 58px;  background: var(--room-one); }
  .door-panel--two   { left: 489px; top: 58px;  background: var(--room-two); }
  .door-panel--three { left: 783px; top: 58px;  background: var(--room-three); }
  .door-panel--four  { left: 186px; top: 641px; background: var(--room-four); }
  .door-panel--five  { left: 489px; top: 641px; background: var(--room-five); }
  .door-panel--six   { left: 783px; top: 641px; background: var(--room-six); }

  .room-word {
    position: absolute;
    top: 14px;
    left: 14px;
    writing-mode: vertical-rl;
    transform: rotate(180deg);
    font-family: "Questrial", sans-serif;
    font-size: 72px;
    line-height: 1;
    letter-spacing: 1px;
    color: var(--ink);
    z-index: 2;
  }
  .room-numeral {
    position: absolute;
    inset: 0;
    width: 230px;
    height: 507px;
  }
  .room-numeral text {
    font-family: "Barlow Condensed", sans-serif;
    font-weight: 600;
    font-size: 478px;
    fill: var(--ink);
  }
</style>
</head>
<body>
  <main class="door-set">
    <section class="door-panel door-panel--one">
      <span class="room-word">ONE</span>
      <svg class="room-numeral" viewBox="0 0 230 507"><text x="126" y="501" textLength="98" lengthAdjust="spacingAndGlyphs">1</text></svg>
    </section>
    <section class="door-panel door-panel--two">
      <span class="room-word">TWO</span>
      <svg class="room-numeral" viewBox="0 0 230 507"><text x="58" y="501" textLength="169" lengthAdjust="spacingAndGlyphs">2</text></svg>
    </section>
    <section class="door-panel door-panel--three">
      <span class="room-word">THREE</span>
      <svg class="room-numeral" viewBox="0 0 230 507"><text x="60" y="501" textLength="168" lengthAdjust="spacingAndGlyphs">3</text></svg>
    </section>
    <section class="door-panel door-panel--four">
      <span class="room-word">FOUR</span>
      <svg class="room-numeral" viewBox="0 0 230 507"><text x="50" y="501" textLength="178" lengthAdjust="spacingAndGlyphs">4</text></svg>
    </section>
    <section class="door-panel door-panel--five">
      <span class="room-word">FIVE</span>
      <svg class="room-numeral" viewBox="0 0 230 507"><text x="62" y="501" textLength="164" lengthAdjust="spacingAndGlyphs">5</text></svg>
    </section>
    <section class="door-panel door-panel--six">
      <span class="room-word">SIX</span>
      <svg class="room-numeral" viewBox="0 0 230 507"><text x="64" y="501" textLength="160" lengthAdjust="spacingAndGlyphs">6</text></svg>
    </section>
  </main>
</body>
</html>
```